The Brandling Firm

We need a new design for our letterhead and envelopes. We are a personal injury and criminal defense firm so we need something modern and clean, but more on the professional/traditional side. Our new logo has two colors and is attached to the file so we need something that works well with those colors/matches the design. The following information needs to be on the letterhead:
Phone: (555) 314-2716
Fax: (555) 314-5093
Toll-Free: (800) 555-0143
Post Office Box 4372
Fernwick, OR 29548-4372
QVHarmCounselGroup.example
MarrowvaleTrialCounsel.example

Target Market(s)

Clients, government agencies, other law firms

Industry/Entity Type

Legal

Font styles to use
Sans Serif
Other font styles liked:
• Arial

Colors

Designer to choose colors to be used in the design.

Requirements
Must have
• Must look professional and clean, modern
Nice to have
• I would like to see a design that works with the logo but does not distract from the content that will be printed on it
Should not have
• Too many colors or crazy designs.

```html
<!DOCTYPE html>
<html lang="en">
<head>
<meta charset="utf-8">
<title>The Brandling Firm — Stationery</title>
<link href="https://fonts.googleapis.com/css2?family=Work+Sans:wght@400;500;600&family=Libre+Baskerville&display=swap" rel="stylesheet">
<style>
  :root {
    --navy: #2b2f8e;
    --navy-dark: #23277a;
    --red: #cf2a2c;
    --ink: #4a4a55;
    --paper: #ffffff;
    --backdrop: #e9e9e9;
  }
  * { box-sizing: border-box; margin: 0; padding: 0; }
  html, body { width: 1200px; height: 900px; overflow: hidden; }
  body {
    background: var(--backdrop);
    font-family: "Work Sans", Arial, sans-serif;
    color: var(--ink);
    position: relative;
  }
  .sheet { position: absolute; background: var(--paper); box-shadow: 0 2px 10px rgba(0,0,0,.12); overflow: hidden; }

  .brand-name {
    font-family: "Work Sans", Arial, sans-serif;
    font-weight: 600;
    color: var(--navy);
    text-transform: uppercase;
    letter-spacing: .06em;
    display: flex; align-items: center; gap: 8px;
    line-height: 1.1;
  }
  .brand-name .dot { width: 10px; height: 10px; border-radius: 50%; background: var(--navy); flex: none; }
  .brand-name.on-dark { color: #fff; }
  .brand-name.on-dark .dot { background: #fff; }

  .footer-band {
    position: absolute; left: 0; right: 0; bottom: 0;
    background: var(--navy);
    color: #fff;
    display: flex; align-items: center; justify-content: flex-end;
    font-size: 11px; letter-spacing: .08em;
    border-top: 3px solid #fff;
    box-shadow: 0 -3px 0 var(--red);
    white-space: nowrap;
  }

  /* Letterhead */
  .letterhead { left: 40px; top: 40px; width: 510px; height: 720px; }
  .letterhead .header { position: absolute; left: 44px; top: 52px; right: 44px; display: flex; align-items: center; }
  .letterhead .brand-name { font-size: 17px; width: 200px; }
  .letterhead .divider { width: 2px; height: 54px; background: var(--red); margin: 0 22px 0 20px; }
  .contact-list { list-style: none; font-size: 8.5px; color: var(--navy); line-height: 1.65; }
  .contact-list li { display: flex; align-items: center; gap: 6px; white-space: nowrap; }
  .contact-list svg { width: 8px; height: 8px; fill: var(--navy); flex: none; }
  .contact-list em { font-style: italic; font-weight: 600; }
  .greeting { position: absolute; left: 44px; top: 196px; font-family: "Libre Baskerville", Georgia, serif; font-size: 18px; font-weight: 400; color: var(--navy); }
  .letter-body { position: absolute; left: 44px; top: 238px; width: 420px; font-size: 9.5px; line-height: 1.65; letter-spacing: .02em; }
  .letter-body p { margin-bottom: 12px; }
  .signoff { position: absolute; left: 44px; top: 540px; font-family: "Libre Baskerville", Georgia, serif; font-size: 14px; color: var(--ink); }
  .signature { position: absolute; left: 44px; top: 566px; width: 120px; height: 30px; background: linear-gradient(90deg, rgba(43,47,142,.18), rgba(43,47,142,.06)); border-radius: 3px; }
  .letterhead .footer-band { height: 56px; padding-right: 34px; font-size: 12px; }

  /* Envelope front */
  .envelope-front { left: 590px; top: 40px; width: 570px; height: 260px; }
  .envelope-front .brand-name { position: absolute; right: 38px; top: 150px; font-size: 15px; }
  .envelope-front .footer-band { height: 30px; padding-right: 22px; font-size: 9.5px; }

  /* Envelope back */
  .envelope-back { left: 590px; top: 320px; width: 570px; height: 260px; background: var(--navy); }
  .envelope-back svg { position: absolute; inset: 0; }

  /* Cards */
  .card { width: 270px; height: 160px; }
  .card-front { left: 590px; top: 610px; background: var(--navy); display: flex; align-items: center; justify-content: center; }
  .card-front .brand-name { font-size: 14px; }
  .card-back { left: 890px; top: 610px; display: flex; justify-content: space-between; padding: 30px 22px; }
  .card-back .brand-name { font-size: 11px; align-self: flex-start; margin-top: 28px; }
  .card-details { font-family: "Libre Baskerville", Georgia, serif; font-size: 7px; line-height: 1.55; color: var(--ink); text-align: left; }
  .card-details p + p { margin-top: 8px; }
</style>
</head>
<body>

<section class="sheet letterhead">
  <header class="header">
    <div class="brand-name"><span class="dot"></span>The Brandling Firm</div>
    <div class="divider"></div>
    <ul class="contact-list">
      <li><svg viewBox="0 0 10 10"><rect x="2.5" y="0.5" width="5" height="9" rx="1"/></svg>(555) 314-2716</li>
      <li><svg viewBox="0 0 10 10"><rect x="1" y="3" width="8" height="5" rx="1"/><rect x="3" y="1" width="4" height="2"/></svg>(555) 314-5093</li>
      <li><svg viewBox="0 0 10 10"><path d="M2 1h2l1 2.5-1.2 1a5 5 0 0 0 2.7 2.7l1-1.2L10 7v2a1 1 0 0 1-1 1A8 8 0 0 1 1 2a1 1 0 0 1 1-1z"/></svg>(800) 555-0143 <em>(Toll Free)</em></li>
      <li><svg viewBox="0 0 10 10"><circle cx="5" cy="5" r="4.5"/></svg>QVHarmCounselGroup.example</li>
      <li><svg viewBox="0 0 10 10"><circle cx="5" cy="5" r="4.5"/></svg>MarrowvaleTrialCounsel.example</li>
    </ul>
  </header>

  <h1 class="greeting">Hello Smith,</h1>
  <div class="letter-body">
    <p>Lorem ipsum dolor sit amet, consectetur adipisicing elit, sed do eiusmod tempor incididunt ut labore et dolore magna aliqua. Ut enim ad minim veniam, quis nostrud exercitation ullamco laboris nisi ut aliquip ex ea commodo consequat. Duis aute irure dolor in reprehenderit in voluptate velit esse cillum dolore eu fugiat nulla pariatur. Excepteur sint occaecat cupidatat non proident, sunt in culpa qui officia deserunt mollit anim id est laborum. Sed ut perspiciatis unde omnis iste natus error sit voluptatem accusantium doloremque laudantium,</p>
    <p>Lorem ipsum dolor sit amet, consectetur adipisicing elit, sed do eiusmod tempor incididunt ut labore et dolore magna aliqua. Ut enim ad minim veniam, quis nostrud exercitation ullamco laboris nisi ut aliquip ex ea commodo consequat.</p>
    <p>Lorem ipsum dolor sit amet, consectetur adipisicing elit, sed do eiusmod tempor incididunt ut labore et dolore magna aliqua.</p>
  </div>
  <p class="signoff">Jordan Vale</p>
  <div class="signature" role="img" aria-label="Handwritten signature"></div>

  <footer class="footer-band">Post Office Box 4372 Fernwick, OR 29548-4372</footer>
</section>

<section class="sheet envelope-front">
  <div class="brand-name"><span class="dot"></span>The Brandling Firm</div>
  <footer class="footer-band">Post Office Box 4372 Fernwick, OR 29548-4372 | MarrowvaleTrialCounsel.example</footer>
</section>

<section class="sheet envelope-back">
  <svg viewBox="0 0 570 260" preserveAspectRatio="none" aria-hidden="true">
    <path d="M0 0 L40 80 Q45 92 60 92 L510 92 Q525 92 530 80 L570 0 Z" fill="var(--navy-dark)" opacity=".55"/>
    <path d="M0 0 L40 80 Q45 92 60 92 L510 92 Q525 92 530 80 L570 0" fill="none" stroke="#1e2270" stroke-width="1.5"/>
  </svg>
</section>

<section class="sheet card card-front">
  <div class="brand-name on-dark"><span class="dot"></span>The Brandling Firm</div>
</section>

<section class="sheet card card-back">
  <div class="brand-name"><span class="dot"></span>The Brandling Firm</div>
  <div class="card-details">
    <p>Elmfield Row 22<br>Fernwick OR</p>
    <p>(555) 314-8820</p>
    <p>office@brandling.example<br>www.brandling.example</p>
  </div>
</section>

</body>
</html>
```